Packaging for a new tea company

Hi guys we need a new packaging design for a tea company we are starting

Our competitors are leafara, zo ren tea

I have uploaded pictures of our competitors for you to see the sample
The label need to be catchy

Our brand is called #PlumVexaTea
We need two packaging designs one for Day Tea and one for calmora

Detox - slim - cleanse

Also needs to says 14 Day Orvalin

Target Market(s)

Young people

Industry/Entity Type

It Company

Colors
000000

Requirements
Must have
• #plumvexatea
Nice to have
• Herbal tea supplement 50gram
• Max label size 13.5cm x 16.5 cm
• Personally I like the paper brown bag as it looks like a higher quality and as the label is a sticker I think this would make the product look a lot better
Should not have
• Nothing

```html
<!DOCTYPE html>
<html lang="en">
<head>
<meta charset="utf-8">
<title>PlumVexaTea – Day Tea Label</title>
<link rel="stylesheet" href="https://fonts.googleapis.com/css2?family=Roboto+Condensed:wght@400;700&display=swap">
<style>
  :root {
    --page-bg: #e4e4e4;
    --label-grey: #7d7e82;
    --frame-line: #d9d9db;
    --brand-red: #b51d2c;
    --text-white: #ffffff;
  }
  * { margin: 0; padding: 0; box-sizing: border-box; }
  html, body { width: 800px; height: 1200px; overflow: hidden; }
  body {
    background: var(--page-bg);
    font-family: "Roboto Condensed", "Arial Narrow", sans-serif;
    position: relative;
  }
  .label {
    position: absolute;
    left: 120px;
    top: 250px;
    width: 560px;
    height: 700px;
    background: var(--label-grey);
  }
  .label-frame {
    position: absolute;
    top: 24px;
    left: 14px;
    right: 14px;
    bottom: 18px;
    border: 1.5px solid var(--frame-line);
  }
  .rule {
    position: absolute;
    left: 112px;
    width: 336px;
    height: 3px;
    background: var(--brand-red);
  }
  .rule-top { top: 118px; }
  .rule-bottom { top: 229px; }
  .brand-name {
    position: absolute;
    top: 138px;
    left: 0;
    width: 100%;
    text-align: center;
    font-size: 62px;
    font-weight: 700;
    line-height: 80px;
    letter-spacing: -0.5px;
    color: var(--text-white);
  }
  .product-type {
    position: absolute;
    top: 248px;
    left: 0;
    width: 100%;
    text-align: center;
    color: var(--brand-red);
  }
  .product-type .type-main {
    display: block;
    font-size: 54px;
    font-weight: 700;
    line-height: 54px;
  }
  .product-type .type-sub {
    display: block;
    font-size: 21px;
    font-weight: 400;
    line-height: 22px;
    letter-spacing: 0.5px;
  }
  .program-badge {
    position: absolute;
    left: 161px;
    top: 360px;
    width: 238px;
    height: 238px;
    border-radius: 50%;
    background: var(--brand-red);
    color: var(--text-white);
    display: flex;
    flex-direction: column;
    align-items: center;
    justify-content: center;
    font-weight: 700;
    text-align: center;
  }
  .program-badge .badge-line {
    font-size: 54px;
    line-height: 56px;
  }
  .tea-time {
    position: absolute;
    left: 181px;
    top: 620px;
    width: 198px;
    height: 47px;
    border: 2px solid var(--text-white);
    border-radius: 24px;
    display: flex;
    align-items: center;
    justify-content: center;
    gap: 8px;
    color: var(--text-white);
    font-size: 25px;
    font-weight: 700;
  }
  .tea-time svg { width: 28px; height: 28px; }
</style>
</head>
<body>
  <section class="label">
    <div class="label-frame"></div>
    <div class="rule rule-top"></div>
    <h1 class="brand-name">PlumVexaTea</h1>
    <div class="rule rule-bottom"></div>
    <p class="product-type">
      <span class="type-main">HERBAL</span>
      <span class="type-sub">TEA SUPPLEMENT</span>
    </p>
    <div class="program-badge">
      <span class="badge-line">14 DAY</span>
      <span class="badge-line">ORVALIN</span>
    </div>
    <div class="tea-time">
      <svg viewBox="0 0 30 30" aria-hidden="true">
        <g fill="none" stroke="#ffffff" stroke-width="1.6" stroke-linecap="round">
          <circle cx="15" cy="15" r="5.5"/>
          <line x1="15" y1="2" x2="15" y2="6"/>
          <line x1="15" y1="24" x2="15" y2="28"/>
          <line x1="2" y1="15" x2="6" y2="15"/>
          <line x1="24" y1="15" x2="28" y2="15"/>
          <line x1="5.8" y1="5.8" x2="8.6" y2="8.6"/>
          <line x1="21.4" y1="21.4" x2="24.2" y2="24.2"/>
          <line x1="5.8" y1="24.2" x2="8.6" y2="21.4"/>
          <line x1="21.4" y1="8.6" x2="24.2" y2="5.8"/>
        </g>
      </svg>
      <span>DAY TEA</span>
    </div>
  </section>
</body>
</html>
```